Brisk Forma - One sheet needed for Sales Team

We need a One Sheet that introduces our business and what we do to prospective customers. This will be used both digitally and print for sales calls, both virtually and in person. Ideally we'd like this to match our branding and messaging from our website briskformahub.com so there is consistency with our messaging. Also, we have a desire for this to have a call to action that directs to our website and main phone where we have lead capture ability.
It should be clean and consistent with current marketing trends. We would like to include information about the business, our value proposition of being able to save customers up to 60% off their copy and printing costs, and some differentiators (i.e. 80+ point inspection of equipment, full teardown and rebuild of like new units, transparent pricing and lease options, 6 month warranty, comprehensive maintenance programs).

```html
<!DOCTYPE html>
<html lang="en">
<head>
<meta charset="UTF-8">
<title>Brisk Forma – One Sheet</title>
<link href="https://fonts.googleapis.com/css2?family=Montserrat:wght@400;500;600;700;800;900&display=swap" rel="stylesheet">
<style>
  :root{
    --magenta:#b03563;
    --blue:#5aa3c7;
    --yellow:#f4ee38;
    --ink:#3a3a3a;
    --ink-soft:#4a4a4a;
    --paper:#ffffff;
  }
  *{margin:0;padding:0;box-sizing:border-box}
  html,body{width:740px;height:1200px;overflow:hidden;background:var(--paper)}
  body{font-family:"Montserrat",Arial,sans-serif;color:var(--ink)}
  .sheet{position:relative;width:740px;height:1200px;overflow:hidden;background:var(--paper)}
  .shapes{position:absolute;inset:0}
  .abs{position:absolute}

  .brand{left:56px;top:70px;display:flex;align-items:center;gap:14px}
  .brand-dot{width:44px;height:44px;border-radius:50%;background:var(--magenta)}
  .brand-name{font-size:40px;font-weight:800;letter-spacing:1px;color:var(--ink);line-height:1}

  .offer{left:53px;top:205px;width:310px}
  .offer-kicker{display:flex;align-items:center;gap:10px;font-size:26px;font-weight:700;color:var(--ink-soft)}
  .offer-kicker::before,.offer-kicker::after{content:"";width:42px;height:2px;background:var(--ink-soft)}
  .offer-big{font-size:64px;font-weight:900;color:var(--magenta);line-height:1.05;margin-top:4px}
  .offer-line{font-size:34px;font-weight:500;color:var(--ink-soft);line-height:1.35;white-space:nowrap}
  .offer-line .hl-blue{color:var(--blue);font-weight:900}
  .offer-line .hl-mag{color:var(--magenta);font-weight:900;font-size:41px}

  .about-tab{left:0;top:460px;width:40px;height:146px;background:var(--blue);display:flex;align-items:center;justify-content:center}
  .about-tab span{transform:rotate(-90deg);white-space:nowrap;color:#fff;font-weight:800;font-size:17px;letter-spacing:.5px}
  .about-text{left:53px;top:464px;width:322px;font-size:12.6px;line-height:1.56;text-align:justify;color:var(--ink-soft)}

  .copier{left:412px;top:640px;width:316px;height:365px;border-radius:40px 40px 30px 30px;
    background:linear-gradient(160deg,#f3f3f3 0%,#d9dade 55%,#2f4f7e 56%,#3b5c8c 64%,#e4e5e8 65%,#c9cace 100%)}

  .pitch{left:65px;top:708px;width:320px;color:#fff}
  .pitch-title{font-size:27px;font-weight:800;line-height:1.2;letter-spacing:.2px;white-space:nowrap}
  .pitch-sub{margin-top:16px;border-left:2px solid #fff;padding-left:11px;font-size:11px;font-weight:500;line-height:1.5;white-space:nowrap}

  .perks{left:50px;top:916px;width:240px;list-style:none}
  .perk{display:flex;align-items:center;gap:16px;height:50px;border-bottom:1px solid rgba(255,255,255,.35);color:#fff;font-size:13.2px;font-weight:500;line-height:1.3}
  .perk:last-child{border-bottom:none}
  .perk-icon{flex:0 0 38px;width:38px;height:38px;border-radius:50%;background:#fff;display:flex;align-items:center;justify-content:center}
  .perk-icon svg{width:22px;height:22px}

  .contact{left:440px;top:1078px;list-style:none}
  .contact li{display:flex;align-items:center;gap:8px;font-size:17px;font-weight:500;color:var(--ink-soft);height:27px;white-space:nowrap}
  .contact svg{flex:0 0 16px;width:16px;height:16px}
  .contact .c-mag{color:var(--magenta)}
  .contact .c-blue{color:var(--blue)}
</style>
</head>
<body>
<main class="sheet">
  <svg class="shapes" width="740" height="1200" viewBox="0 0 740 1200" role="img" aria-label="Photo of a hand pressing keys on an office copier control panel">
    <defs>
      <linearGradient id="officeTones" x1="0" y1="0" x2="1" y2="1">
        <stop offset="0" stop-color="#e8cfa4"/>
        <stop offset=".45" stop-color="#c9c2b8"/>
        <stop offset=".75" stop-color="#a9a8a6"/>
        <stop offset="1" stop-color="#6d6d6f"/>
      </linearGradient>
    </defs>
    <path d="M740 0 L376 0 C365 55 405 110 412 170 C420 235 372 270 374 340 C376 430 410 515 470 555 C540 595 610 590 680 575 L740 560 Z" fill="url(#officeTones)"/>
    <path d="M0 645 C40 640 80 610 128 612 C175 614 190 650 240 652 C300 654 340 615 405 640 C440 660 450 700 430 760 C410 830 460 880 440 950 C420 1020 360 1100 374 1200 L0 1200 Z" fill="var(--magenta)"/>
    <circle cx="396" cy="212" r="19" fill="var(--blue)"/>
    <circle cx="396" cy="267" r="10" fill="var(--magenta)"/>
    <circle cx="701" cy="541" r="12" fill="var(--yellow)"/>
    <circle cx="653" cy="574" r="24" fill="var(--magenta)"/>
    <circle cx="361" cy="1034" r="27" fill="var(--blue)"/>
    <circle cx="423" cy="1013" r="16" fill="var(--magenta)"/>
  </svg>

  <div class="abs brand">
    <span class="brand-dot"></span>
    <span class="brand-name">BRISK FORMA</span>
  </div>

  <section class="abs offer">
    <p class="offer-kicker">Save Up To</p>
    <p class="offer-big">60% Off</p>
    <p class="offer-line">Their <span class="hl-blue">Copy</span> and</p>
    <p class="offer-line"><span class="hl-mag">Printing</span> Costs</p>
  </section>

  <div class="abs about-tab"><span>ABOUT US</span></div>
  <p class="abs about-text">Brisk Forma offers the finest in state of the art equipment from manufacturers such as Rivolt, Calder, and Kovana Mireta. In addition to new equipment, we also rent, lease, and sell refurbished copiers. These copiers are fully reconditioned and warranted to give many years of high quality performance to the cost conscious business.</p>

  <div class="abs copier" role="img" aria-label="Photo of a large multifunction office copier"></div>

  <section class="abs pitch">
    <h2 class="pitch-title">HELPING<br>BUSINESS OWNERS<br>SAVE MONEY</h2>
    <p class="pitch-sub">Smart Office &amp; Work From Home Print Solutions<br>By Rivolt, Calder, Kovana Mireta, Kyrona &amp; Sharwell</p>
  </section>

  <ul class="abs perks">
    <li class="perk"><span class="perk-icon"><svg viewBox="0 0 24 24" fill="none" stroke="#777" stroke-width="1.5"><circle cx="11" cy="11" r="6"/><path d="M15.5 15.5 20 20"/></svg></span><span>80+ point<br>inspection of equipment</span></li>
    <li class="perk"><span class="perk-icon"><svg viewBox="0 0 24 24" fill="none" stroke="#777" stroke-width="1.5"><rect x="6" y="3" width="12" height="18" rx="1"/><path d="M9 8h6M9 12h6M9 16h4"/></svg></span><span>Full teardown and<br>rebuild of like new units</span></li>
    <li class="perk"><span class="perk-icon"><svg viewBox="0 0 24 24" fill="none" stroke="#777" stroke-width="1.5"><circle cx="12" cy="12" r="8"/><path d="M12 7v10M9.5 9.5h4a1.5 1.5 0 0 1 0 3h-3a1.5 1.5 0 0 0 0 3h4"/></svg></span><span>Transparent pricing and<br>lease options</span></li>
    <li class="perk"><span class="perk-icon"><svg viewBox="0 0 24 24" fill="none" stroke="#777" stroke-width="1.5"><path d="M12 3l7 3v5c0 5-3 8-7 10-4-2-7-5-7-10V6z"/><path d="M9 12l2 2 4-4"/></svg></span><span>6 month warranty</span></li>
    <li class="perk"><span class="perk-icon"><svg viewBox="0 0 24 24" fill="none" stroke="#777" stroke-width="1.5"><circle cx="12" cy="12" r="3"/><path d="M12 3v3M12 18v3M3 12h3M18 12h3M5.6 5.6l2.1 2.1M16.3 16.3l2.1 2.1M5.6 18.4l2.1-2.1M16.3 7.7l2.1-2.1"/></svg></span><span>Comprehensive<br>maintenance programs</span></li>
  </ul>

  <ul class="abs contact">
    <li><svg viewBox="0 0 24 24" fill="none" stroke="var(--magenta)" stroke-width="2"><circle cx="12" cy="12" r="10"/><path d="M9 7l1.5 3-1.2 1.2a7 7 0 0 0 3.5 3.5L14 13.5l3 1.5-1 2.5C11 17 7 13 6.5 8z" fill="var(--magenta)" stroke="none"/></svg><span>555-014-2290</span></li>
    <li><svg viewBox="0 0 24 24"><circle cx="12" cy="12" r="11" fill="var(--magenta)"/><rect x="6" y="8" width="12" height="8" fill="none" stroke="#fff" stroke-width="1.5"/><path d="M6 8l6 5 6-5" fill="none" stroke="#fff" stroke-width="1.5"/></svg><span>Info@<span class="c-mag">brisk</span><span class="c-blue">formahub</span>.com</span></li>
    <li><svg viewBox="0 0 24 24" fill="none" stroke="var(--magenta)" stroke-width="1.6"><circle cx="12" cy="12" r="10"/><ellipse cx="12" cy="12" rx="4.5" ry="10"/><path d="M2 12h20M4 7h16M4 17h16"/></svg><span>www.<span class="c-mag">brisk</span><span class="c-blue">formahub</span>.com</span></li>
  </ul>
</main>
</body>
</html>
```